Orvel Prime - Letter Head

My company is a residential and commercial cleaning company , which is located in Abu Dhabi, UAE.
I am looking for a creative letterhead reflects the professional and reflects professionalism and send the feeling of relax and comfort.
The color which will be used it has to be selected carefully in prospective of colors psychological effects, so every color to be used should be for a reason.
Also, reflecting my company colors in an attractive way.
Regarding the information which it should contains, it has to show the address, contacts , telephones an, email address and website.
Also, my company logo is attached
Residential

```html
<!DOCTYPE html>
<html lang="en">
<head>
<meta charset="utf-8">
<title>Orvel Prime – Stationery</title>
<link rel="stylesheet" href="https://fonts.googleapis.com/css2?family=Montserrat:wght@400;600;700&family=Oswald:wght@400;500&display=swap">
<style>
  :root {
    --bg: #e8e9ea;
    --paper: #ffffff;
    --brand-blue: #1f6db5;
    --brand-green: #8cc63f;
    --ink: #4a4f55;
    --ink-soft: #8a9096;
    --ink-dark: #2b2f33;
    --grey-mark: #6b6f73;
    --leaf-blue: #3d8fd0;
    --leaf-sky: #8fcbe8;
    --leaf-orange: #f2a23c;
    --leaf-green: #9ccc4e;
    --leaf-navy: #2a5ea8;
    --shadow: 0 2px 6px rgba(0,0,0,.08);
  }
  * { box-sizing: border-box; margin: 0; padding: 0; }
  html, body { width: 1200px; height: 1200px; overflow: hidden; }
  body {
    background: var(--bg);
    position: relative;
    font-family: "Montserrat", Arial, sans-serif;
    color: var(--ink);
  }

  .sheet { position: absolute; background: var(--paper); box-shadow: var(--shadow); overflow: hidden; }

  /* wordmark */
  .wordmark { display: flex; align-items: center; gap: 5px; }
  .wordmark .name { font-family: "Montserrat", Arial, sans-serif; font-weight: 700; color: var(--brand-blue); line-height: 1; letter-spacing: -0.02em; }
  .wordmark .dot { border-radius: 50%; background: var(--brand-green); flex: none; }
  .wordmark.mono .name { color: var(--grey-mark); }
  .wordmark.mono .dot { background: #b5b8bb; }
  .wordmark.light .name { color: #ffffff; }
  .wordmark.light .dot { background: #ffffff; }

  /* leaf pattern band placeholder */
  .leaf-band {
    position: absolute; left: 0; right: 0;
    background: linear-gradient(90deg,
      var(--leaf-sky) 0%, var(--leaf-blue) 12%, var(--leaf-orange) 22%, var(--leaf-sky) 32%,
      var(--leaf-navy) 44%, var(--leaf-green) 54%, var(--leaf-orange) 64%, var(--leaf-blue) 76%,
      var(--leaf-sky) 86%, var(--leaf-green) 100%);
    opacity: .55;
  }

  /* letterhead */
  .letterhead { top: 300px; width: 310px; height: 432px; }
  .letterhead.color { left: 94px; }
  .letterhead.mono { left: 432px; }
  .letterhead .wordmark { position: absolute; left: 22px; top: 28px; }
  .letterhead .wordmark .name { font-size: 13px; }
  .letterhead .wordmark .dot { width: 12px; height: 12px; }
  .letterhead .accent-bar { position: absolute; right: 0; top: 22px; width: 3px; height: 20px; background: var(--brand-green); }
  .letterhead.mono .accent-bar { background: #9a9da0; }

  .contact-block { position: absolute; top: 24px; left: 182px; display: flex; gap: 14px; font-size: 4.3px; line-height: 1.7; color: var(--ink); }
  .contact-block .col { display: flex; flex-direction: column; }
  .contact-block .row { display: flex; align-items: flex-start; gap: 3px; }
  .contact-block svg { width: 5px; height: 5px; flex: none; margin-top: 1px; }
  .letterhead.color .contact-block svg { fill: var(--brand-blue); }
  .letterhead.mono .contact-block svg { fill: var(--grey-mark); }

  .letter-body { position: absolute; left: 50px; right: 28px; top: 108px; font-size: 4.1px; line-height: 1.75; color: var(--ink-soft); }
  .letter-body .meta { color: var(--ink-dark); font-weight: 600; font-style: italic; margin-bottom: 8px; }
  .letter-body .salute { margin-bottom: 3px; }
  .letter-body p { margin-bottom: 8px; }

  .sign-off { position: absolute; left: 50px; top: 282px; }
  .sign-off .signer { font-size: 7px; font-weight: 600; color: var(--ink-dark); letter-spacing: .02em; }
  .sign-off .signer span { font-weight: 400; }
  .sign-off .role { font-size: 4.5px; color: var(--ink-soft); }
  .signature-area { position: absolute; left: 50px; top: 318px; width: 70px; height: 30px; background: #f1f2f3; border-radius: 3px; }

  /* folder */
  .folder { left: 780px; top: 274px; width: 336px; height: 462px; }
  .folder .wordmark { position: absolute; right: 30px; top: 48px; }
  .folder .wordmark .name { font-size: 30px; }
  .folder .wordmark .dot { width: 26px; height: 26px; }
  .folder .leaf-band { top: 386px; height: 50px; }
  .folder .spine { position: absolute; left: 0; top: 0; bottom: 0; width: 10px; background: linear-gradient(90deg, #f2f3f4, #ffffff); }

  /* envelopes */
  .envelope { top: 763px; height: 160px; }
  .envelope.front { left: 86px; width: 316px; }
  .envelope.back { left: 436px; width: 318px; }
  .envelope.front .wordmark { position: absolute; left: 18px; top: 24px; }
  .envelope.front .wordmark .name { font-size: 17px; }
  .envelope.front .wordmark .dot { width: 15px; height: 15px; }
  .envelope.front .leaf-band { bottom: 4px; height: 34px; }
  .envelope.back .leaf-band { top: 0; height: 36px; }
  .return-address { position: absolute; right: 32px; bottom: 28px; text-align: right; font-family: "Oswald", Arial, sans-serif; font-size: 5.4px; line-height: 1.35; color: var(--brand-blue); }
  .return-address .co { font-weight: 500; font-size: 6.2px; color: var(--ink-dark); }
  .envelope.back .mark-dot { position: absolute; right: 14px; bottom: 32px; width: 13px; height: 13px; border-radius: 50%; background: var(--brand-green); }

  /* business cards */
  .card { top: 758px; width: 134px; height: 78px; }
  .card.front { left: 790px; }
  .card.back { left: 978px; width: 132px;
    background: linear-gradient(120deg, var(--leaf-navy) 0%, var(--leaf-sky) 45%, var(--leaf-green) 75%, var(--leaf-orange) 100%); }
  .card.front .wordmark { position: absolute; left: 10px; top: 9px; }
  .card.front .wordmark .name { font-size: 8.5px; }
  .card.front .wordmark .dot { width: 7px; height: 7px; }
  .card .holder { position: absolute; left: 10px; top: 34px; font-family: "Oswald", Arial, sans-serif; font-size: 5px; color: var(--brand-blue); font-weight: 500; }
  .card .holder span { color: var(--ink-soft); font-weight: 400; }
  .card .details { position: absolute; left: 10px; top: 44px; display: flex; gap: 12px; font-size: 3.4px; line-height: 1.7; color: var(--brand-blue); }
  .card .details .col { display: flex; flex-direction: column; }
  .card .details .row { display: flex; align-items: center; gap: 2px; }
  .card .details i { width: 3px; height: 3px; border-radius: 50%; background: var(--leaf-orange); display: inline-block; }
  .card.back .wordmark { position: absolute; left: 0; right: 0; top: 30px; justify-content: center; }
  .card.back .wordmark .name { font-size: 12px; }
  .card.back .wordmark .dot { width: 10px; height: 10px; }
</style>
</head>
<body>

  <!-- colour letterhead -->
  <section class="sheet letterhead color">
    <div class="wordmark"><span class="name">Orvel Prime</span><span class="dot"></span></div>
    <div class="accent-bar"></div>
    <div class="contact-block">
      <div class="col">
        <div class="row"><svg viewBox="0 0 10 10"><path d="M5 0a3.5 3.5 0 0 0-3.5 3.5C1.5 6 5 10 5 10s3.5-4 3.5-6.5A3.5 3.5 0 0 0 5 0zm0 5a1.5 1.5 0 1 1 0-3 1.5 1.5 0 0 1 0 3z"/></svg><span>Orvel Prime, Inc.<br>14 Harbor Lane<br>Postal Code, City</span></div>
      </div>
      <div class="col">
        <div class="row"><svg viewBox="0 0 10 10"><path d="M2 0l2 2.5-1 1.2a6 6 0 0 0 3.3 3.3l1.2-1L10 8l-1.5 2C4 10 0 6 0 1.5z"/></svg><span>555 014 220</span></div>
        <div class="row"><svg viewBox="0 0 10 10"><path d="M0 2h10v6H0zM0 2l5 3.5L10 2"/></svg><span>info@orvelprime.com</span></div>
        <div class="row"><svg viewBox="0 0 10 10"><circle cx="5" cy="5" r="5"/></svg><span>www.orvelprime.com</span></div>
      </div>
    </div>
    <div class="letter-body">
      <div class="meta">Date: Mon, 05 / 3 / 2032<br>Recipient: Mr. Elias Brandt</div>
      <div class="salute">Dear Mr. Brandt,</div>
      <p>Thank you for choosing our team to care for your home and office spaces. We plan each visit around your schedule, bring our own safe supplies and leave every room fresh, calm and ready to use. Our staff are trained, insured and careful with every surface they touch.</p>
      <p>Please find the service plan attached to this letter. It lists the rooms covered, the weekly visits agreed and the products we use, all chosen to be gentle on people and on the planet.</p>
      <p>Should you wish to change any detail, simply reply to this letter or call our office. We look forward to welcoming you as a client and to keeping your spaces clean and bright.</p>
    </div>
    <div class="sign-off">
      <div class="signer">MARA <span>LIND</span></div>
      <div class="role">General director</div>
    </div>
    <div class="signature-area" role="img" aria-label="Handwritten signature of the general director"></div>
  </section>

  <!-- greyscale letterhead -->
  <section class="sheet letterhead mono">
    <div class="wordmark mono"><span class="name">Orvel Prime</span><span class="dot"></span></div>
    <div class="accent-bar"></div>
    <div class="contact-block">
      <div class="col">
        <div class="row"><svg viewBox="0 0 10 10"><path d="M5 0a3.5 3.5 0 0 0-3.5 3.5C1.5 6 5 10 5 10s3.5-4 3.5-6.5A3.5 3.5 0 0 0 5 0zm0 5a1.5 1.5 0 1 1 0-3 1.5 1.5 0 0 1 0 3z"/></svg><span>Orvel Prime, Inc.<br>14 Harbor Lane<br>Postal Code, City</span></div>
      </div>
      <div class="col">
        <div class="row"><svg viewBox="0 0 10 10"><path d="M2 0l2 2.5-1 1.2a6 6 0 0 0 3.3 3.3l1.2-1L10 8l-1.5 2C4 10 0 6 0 1.5z"/></svg><span>555 014 220</span></div>
        <div class="row"><svg viewBox="0 0 10 10"><path d="M0 2h10v6H0zM0 2l5 3.5L10 2"/></svg><span>info@orvelprime.com</span></div>
        <div class="row"><svg viewBox="0 0 10 10"><circle cx="5" cy="5" r="5"/></svg><span>www.orvelprime.com</span></div>
      </div>
    </div>
    <div class="letter-body">
      <div class="meta">Date: Mon, 05 / 3 / 2032<br>Recipient: Mr. Elias Brandt</div>
      <div class="salute">Dear Mr. Brandt,</div>
      <p>Thank you for choosing our team to care for your home and office spaces. We plan each visit around your schedule, bring our own safe supplies and leave every room fresh, calm and ready to use. Our staff are trained, insured and careful with every surface they touch.</p>
      <p>Please find the service plan attached to this letter. It lists the rooms covered, the weekly visits agreed and the products we use, all chosen to be gentle on people and on the planet.</p>
      <p>Should you wish to change any detail, simply reply to this letter or call our office. We look forward to welcoming you as a client and to keeping your spaces clean and bright.</p>
    </div>
    <div class="sign-off">
      <div class="signer">MARA <span>LIND</span></div>
      <div class="role">General director</div>
    </div>
    <div class="signature-area" role="img" aria-label="Handwritten signature of the general director"></div>
  </section>

  <!-- presentation folder -->
  <section class="sheet folder">
    <div class="spine"></div>
    <div class="wordmark"><span class="name">Orvel Prime</span><span class="dot"></span></div>
    <div class="leaf-band" role="img" aria-label="Decorative band of interlocking rings and leaves in blue, green and orange"></div>
  </section>

  <!-- envelope front -->
  <section class="sheet envelope front">
    <div class="wordmark"><span class="name">Orvel Prime</span><span class="dot"></span></div>
    <div class="leaf-band" role="img" aria-label="Decorative band of interlocking rings and leaves in blue, green and orange"></div>
  </section>

  <!-- envelope back -->
  <section class="sheet envelope back">
    <div class="leaf-band" role="img" aria-label="Decorative band of interlocking rings and leaves in blue, green and orange"></div>
    <div class="return-address">
      <div class="co">ORVEL PRIME INC</div>
      <div>14 Harbor Lane No 115</div>
      <div>Your Town</div>
      <div>Postal Code</div>
    </div>
    <span class="mark-dot"></span>
  </section>

  <!-- business card front -->
  <section class="sheet card front">
    <div class="wordmark"><span class="name">Orvel Prime</span><span class="dot"></span></div>
    <div class="holder">TOMAS REYES <span>| DIRECTOR</span></div>
    <div class="details">
      <div class="col">
        <div class="row"><i></i>14 Harbor Lane No 115</div>
        <div class="row"><i></i>Your Town</div>
        <div class="row"><i></i>Postal Code</div>
      </div>
      <div class="col">
        <div class="row"><i></i>555 014 220</div>
        <div class="row"><i></i>www.orvelprime.com</div>
        <div class="row"><i></i>info@orvelprime.com</div>
      </div>
    </div>
  </section>

  <!-- business card back -->
  <section class="sheet card back">
    <div class="wordmark light"><span class="name">Orvel Prime</span><span class="dot"></span></div>
  </section>

</body>
</html>
```